Health and Wellness company needs flyer to promote free seminar

Stride reform studio is a health and wellness company that offers an exercise program designed by physical therapists to help relieve pain and improve mobility. Our business is a new concept that is not well understood by the public. In order to promote our business we offer a free seminar where we present information regarding the underlying cause of pain and tightness. During the seminar we also perform a posture screen and movement testing for all participants.

Target Market(s)

Mostly healthy and active women ages 25-65

Industry/Entity Type

Health And Wellness

Font styles to use
Sans Serif

Colors

Designer to choose colors to be used in the design.

Requirements
Must have
• Title: Eliminate Pain and Tightness For Good
• Paragraph: Stride Reform Studio offers a free 60 minute seminar: "The Busy Walker's Handbook to Bending and Standing Taller."
• What to Expect:
• • Identify the underlying cause of your pain and mobility issues
• • Expose what gets in the way of you moving and feeling better
• • Learn why traditional exercises don’t help and can actually make the problem worse
• • Reveal what your posture is saying and how that impacts you
• • Experience your muscle imbalances through movement tests
• • Discover the training method that realigns your posture, increases your mobility and reduces your pain
• Call to action: RSVP online at stridereformstudio.com
Nice to have
• Use a relevant image showing a female dealing with tightness in the low back, legs, etc.
• Emphasize that the seminar is FREE.
• Make the call to action prominent.

```html
<!DOCTYPE html>
<html lang="en">
<head>
<meta charset="utf-8">
<title>Stride Reform Studio – Free Seminar Flyer</title>
<link rel="stylesheet" href="https://fonts.googleapis.com/css2?family=Questrial&family=Mulish:wght@600;700&family=Lato:wght@400;700&display=swap">
<style>
  :root {
    --backdrop: #dedfe0;
    --orange: #f5921e;
    --indigo: #4f4f9c;
    --indigo-deep: #3f4385;
    --ink: #2b2b2b;
    --white: #ffffff;
    --check: #4b56a6;
  }
  * { margin: 0; padding: 0; box-sizing: border-box; }
  html, body { width: 1200px; height: 1200px; overflow: hidden; background: var(--backdrop); }
  .flyer {
    position: absolute; left: 213px; top: 59px;
    width: 773px; height: 1085px;
    background: var(--white);
    box-shadow: 0 4px 14px rgba(0,0,0,.25);
    overflow: hidden;
  }
  .title-column {
    position: absolute; left: 0; top: 0; width: 198px; height: 954px;
    background: var(--orange);
  }
  .title-column svg { position: absolute; left: 0; top: 0; }
  .title-text {
    position: absolute; left: 0; top: 930px;
    width: 900px; height: 198px;
    transform-origin: 0 0; transform: rotate(-90deg);
    font-family: "Questrial", sans-serif; color: var(--white);
    white-space: nowrap;
  }
  .title-line {
    position: absolute; font-size: 57px; line-height: 1;
  }
  .title-line.main { left: 46px; top: 34px; letter-spacing: -0.5px; }
  .title-line.emphasis { left: 297px; top: 104px; letter-spacing: 1px; }
  .hero-photo { position: absolute; left: 198px; top: 0; width: 575px; height: 540px; }
  .seminar {
    position: absolute; left: 218px; top: 494px; width: 540px;
    font-family: "Mulish", sans-serif;
  }
  .seminar-host { font-size: 22px; font-weight: 700; color: var(--ink); }
  .seminar-offer { font-size: 35px; font-weight: 700; color: var(--indigo); margin-top: 4px; line-height: 1.1; }
  .seminar-offer span { color: var(--ink); }
  .seminar-title { font-size: 27px; font-weight: 700; color: var(--orange); line-height: 1.28; margin-top: 10px; }
  .expect {
    position: absolute; left: 220px; top: 660px; width: 530px;
    font-family: "Lato", sans-serif; color: var(--ink);
  }
  .expect h2 { font-size: 21px; font-weight: 700; text-decoration: underline; text-underline-offset: 3px; margin-bottom: 13px; }
  .expect ul { list-style: none; }
  .expect li {
    position: relative; padding-left: 23px;
    font-size: 17px; line-height: 21px; margin-bottom: 10px;
  }
  .expect li svg { position: absolute; left: 0; top: 3px; }
  .footer {
    position: absolute; left: 0; top: 954px; width: 773px; height: 131px;
    background: linear-gradient(90deg, var(--indigo-deep), var(--indigo) 50%, var(--indigo-deep));
    color: var(--white); font-family: "Lato", sans-serif;
  }
  .cta { position: absolute; left: 40px; top: 41px; font-size: 21px; line-height: 27px; }
  .cta strong { font-weight: 700; }
  .brand {
    position: absolute; left: 478px; top: 40px; display: flex; align-items: center; gap: 10px;
    font-family: "Lato", sans-serif; font-size: 24px; font-weight: 400; color: var(--white);
  }
  .brand-square { width: 48px; height: 48px; border: 3px solid var(--white); border-radius: 4px; }
</style>
</head>
<body>
  <main class="flyer">
    <section class="title-column">
      <svg width="198" height="954" aria-hidden="true">
        <polyline points="29,64 29,38 166,38 166,64" fill="none" stroke="#fff" stroke-width="6"/>
        <polyline points="29,886 29,912 166,912 166,886" fill="none" stroke="#fff" stroke-width="6"/>
      </svg>
      <h1 class="title-text">
        <span class="title-line main">Eliminate Pain and Tightness</span>
        <span class="title-line emphasis">FOR GOOD</span>
      </h1>
    </section>

    <svg class="hero-photo" viewBox="0 0 575 540" role="img" aria-label="Photo of a woman running along a tree-lined road">
      <defs>
        <linearGradient id="scene" x1="0" y1="0" x2="0" y2="1">
          <stop offset="0" stop-color="#7f9a4e"/>
          <stop offset="0.45" stop-color="#6f8a45"/>
          <stop offset="0.62" stop-color="#9a9a7a"/>
          <stop offset="0.75" stop-color="#8b8e92"/>
          <stop offset="0.88" stop-color="#c9cacc"/>
          <stop offset="1" stop-color="#ffffff"/>
        </linearGradient>
        <linearGradient id="sky" x1="0" y1="0" x2="1" y2="0">
          <stop offset="0" stop-color="#ffffff" stop-opacity="0"/>
          <stop offset="0.5" stop-color="#eef2f0" stop-opacity="0.75"/>
          <stop offset="1" stop-color="#ffffff" stop-opacity="0"/>
        </linearGradient>
      </defs>
      <rect width="575" height="540" fill="url(#scene)"/>
      <rect y="0" width="575" height="330" fill="url(#sky)"/>
    </svg>

    <section class="seminar">
      <p class="seminar-host">Stride Reform Studio offers a</p>
      <p class="seminar-offer">Free 60 minute seminar<span>:</span></p>
      <p class="seminar-title">"The Busy Walker's Handbook to Bending and Standing Taller."</p>
    </section>

    <section class="expect">
      <h2>What to Expect:</h2>
      <ul>
        <li><svg width="18" height="16" aria-hidden="true"><rect x="1" y="3" width="12" height="12" fill="none" stroke="#4b56a6" stroke-width="1.6"/><polyline points="3,8 7,12 17,1" fill="none" stroke="#4b56a6" stroke-width="2.4"/></svg>Identify the underlying cause of your pain and mobility issues</li>
        <li><svg width="18" height="16" aria-hidden="true"><rect x="1" y="3" width="12" height="12" fill="none" stroke="#4b56a6" stroke-width="1.6"/><polyline points="3,8 7,12 17,1" fill="none" stroke="#4b56a6" stroke-width="2.4"/></svg>Expose what gets in the way of you moving and feeling better</li>
        <li><svg width="18" height="16" aria-hidden="true"><rect x="1" y="3" width="12" height="12" fill="none" stroke="#4b56a6" stroke-width="1.6"/><polyline points="3,8 7,12 17,1" fill="none" stroke="#4b56a6" stroke-width="2.4"/></svg>Learn why traditional exercises don’t help and can actually make the problem worse</li>
        <li><svg width="18" height="16" aria-hidden="true"><rect x="1" y="3" width="12" height="12" fill="none" stroke="#4b56a6" stroke-width="1.6"/><polyline points="3,8 7,12 17,1" fill="none" stroke="#4b56a6" stroke-width="2.4"/></svg>Reveal what your posture is saying and how that impacts you</li>
        <li><svg width="18" height="16" aria-hidden="true"><rect x="1" y="3" width="12" height="12" fill="none" stroke="#4b56a6" stroke-width="1.6"/><polyline points="3,8 7,12 17,1" fill="none" stroke="#4b56a6" stroke-width="2.4"/></svg>Experience your muscle imbalances through movement tests</li>
        <li><svg width="18" height="16" aria-hidden="true"><rect x="1" y="3" width="12" height="12" fill="none" stroke="#4b56a6" stroke-width="1.6"/><polyline points="3,8 7,12 17,1" fill="none" stroke="#4b56a6" stroke-width="2.4"/></svg>Discover the training method that realigns your posture, increases your mobility and reduces your pain</li>
      </ul>
    </section>

    <footer class="footer">
      <p class="cta">Sign up online at<br><strong>stridereformstudio.com/free-seminar</strong></p>
      <div class="brand"><span class="brand-square"></span><span>stridereformstudio</span></div>
    </footer>
  </main>
</body>
</html>
```